Website design for Australia Equine Insurance business

Website Design Brief
1. Introduction
This brief guides the development of a modern, interactive website for our next-generation equine insurance business. We aim to establish a strong digital presence with a website that embodies innovation, usability, and trust, leading to exceptional user experiences and high customer conversions.

2. Company Background
Our startup offers cutting-edge equine insurance solutions across Australia, leveraging emerging technologies for smarter risk assessment, customer engagement, and claims processing. Our commitment is to protect our customers' financial interests and their equine companions with unparalleled service and modern, flexible insurance options.

3. Objectives
The website should:

Highlight our innovative products, services, and unique value proposition.
Drive lead generation and customer conversion using engaging design elements and compelling CTAs.
Foster customer trust and loyalty through transparency, industry expertise, and interactive features.
Enable users to request quotes, purchase insurance, and file claims online in a seamless, intuitive manner.
Be responsive and user-friendly across all devices.

5. Design Requirements
Look and Feel
The design should reflect our brand's personality: innovative, modern, reliable, and committed to the equine community. It should use our brand colours and logo, ensuring a clean, fresh aesthetic. The style guide should promote consistency across fonts, buttons, form fields, etc.

User Interface
The website should display optimally across desktop, tablet, and mobile, with a focus on usability and accessibility. Clear navigation menus, intuitive search and filters, and easy access to important pages like "Get a Quote," "File a Claim," "Contact Us," etc., should be ensured.

Content
Content should be engaging, easily digestible, and serve to educate users about our unique services and the value of equine insurance. The site should also feature blog posts, video guides, and interactive FAQs to illustrate our industry expertise and the benefits of our next-gen approach.

Functionality
Smart Quote Calculator: An AI-driven quote calculator providing real-time estimates.
Digital Purchase and Claims: Facilitate insurance purchase and claims filing digitally, complemented by AI and blockchain tech for efficiency and transparency.
User Accounts: Customers should be able to manage their policies, payments, and claims through personalized accounts.
AI Chatbot: Implement a chatbot for automated customer support, query resolution, and guidance.
SEO and Analytics: Ensure the website is SEO-optimized and integrated with analytics tools like Google Analytics.
6. Timeline
We aim to complete the website design and development project within a 4-month timeframe, given the startup nature of our business. This includes stages of initial design, content creation, development, testing, and launch.

7. Budget
We understand the importance of investing in quality and are open to reasonable negotiations for ensuring the best output.

Target Market(s)

4. Target Audience Our target audience is tech-savvy horse owners, breeders, trainers, equestrian centres, and younger individuals interested in equine ownership, primarily aged between 18-45. They appreciate digital convenience, technological innovation, and quality service.

Industry/Entity Type

The equine insurance industry is a specialised branch of the broader insurance market, focusing on coverage for all things related to horses. It encompasses a wide range of coverage areas such as mortality insurance (life insurance for horses), medical coverage, loss of use, liability coverage, and more. The industry is one of passion and care, where the clientele often form a deeply emotional connection to their insured assets - their horses. It’s characterized by a strong focus on well-being, safety, and the financial protection of both the horses and their owners. This makes trust, professionalism, and expertise central to any successful equine insurance business. Our new venture is positioned as a next-generation equine insurance provider. This means we are blending traditional insurance offerings with cutting-edge technologies such as AI and machine learning for better risk assessment, seamless customer service, and efficient claims processing. The audience in this sector is diverse, ranging from individual horse owners and breeders to professional trainers and large equestrian centres. Many of our customers have a significant emotional and financial investment in their horses, so they need to feel reassured that their insurance provider understands and respects this. In designing for this industry, it's essential to strike a balance between sophistication and warmth, to reflect both our professional reliability and our understanding of the personal passion that drives our clients. The design needs to feel modern and innovative, signaling our next-gen approach, but also trustworthy and user-friendly, ensuring customers of all technological skill levels feel comfortable using our platform. Moreover, the design should convey a sense of our commitment to the equine community, showing that we're more than just a faceless corporation. We care deeply about the wellbeing of horses and their owners, and we're here to support them with quality insurance solutions tailored to their unique needs.

Coding

Coded - Design and coding required

Number of Pages Required

5+ page

Requirements
Must have
• Responsive Design: The website should be fully responsive, offering optimal viewing and interaction across a range of devices - desktop, tablet, and mobile. Intuitive Navigation: The site should feature an easy-to-understand navigation system that allows users to find the information they're seeking quickly and efficiently. Clear Branding: The design should consistently incorporate the company's logo, colors, and overall aesthetic, reinforcing brand recognition. Content: High-quality, relevant content that explains your services, highlights your unique selling propositions, and educates users about equine insurance. The language should be clear, concise, and engaging. Smart Quote Calculator: An interactive tool enabling potential customers to get real-time insurance quotes. Online Purchase and Claims Filing System: A streamlined, user-friendly process for customers to buy insurance and file claims online. Customer Accounts: A secure area for customers to manage their policies, track claims, and make payments. AI Chatbot: An automated chat feature providing immediate customer support and answering frequently asked questions. SEO Optimization: The site must be search engine friendly, with strategically placed keywords, meta tags, and an XML sitemap for better indexing by search engines. Analytics Integration: Integration with tools like Google Analytics for tracking and analyzing user behavior and site performance. Data Security: Implementation of strong security measures to protect user data, including SSL encryption. Accessibility: Compliance with Web Content Accessibility Guidelines (WCAG) to ensure the site is accessible to people with disabilities. Contact Information: Clearly visible and easily accessible contact details, including phone number, email, and physical address. Social Media Integration: Links to the company's social media profiles for enhanced customer engagement and brand visibility. Remember, while these are essential features, the goal should always be to provide a seamless, positive user experience that aligns with your brand's identity and goals.
Nice to have
• Interactive Features: Interactive elements like quizzes or calculators can engage users, offer value, and make your site more memorable. Video Content: Videos explaining your products, services, or the importance of equine insurance can be a dynamic way to share information and appeal to different learning styles. Live Chat: In addition to an AI chatbot, having a live chat option for immediate customer support could significantly enhance user experience and satisfaction. Personalisation: If your resources allow, personalised content based on user behaviour or preferences can make your website more engaging and relevant. Integrated Blog: A blog section featuring articles on equine health, insurance tips, case studies etc., could help establish your brand as a thought leader in the field and improve SEO. Multilingual Support: If your target audience includes non-English speakers, offering content in multiple languages could be a beneficial feature. Customer Testimonials/Reviews: Including testimonials or reviews from satisfied customers can build trust and offer social proof. Resource Library: A library of downloadable resources (guides, checklists, eBooks) could offer added value to your customers and potential leads. Interactive FAQ: A dynamic FAQ section, where users can find answers quickly, or even an FAQ chatbot, could enhance the user experience. Newsletter Signup: An easily accessible sign-up option for a regular newsletter to keep users informed about your services, industry news, and tips. Integration with Customer Relationship Management (CRM) Software: To manage leads and customer information effectively, if your business operations allow for this level of integration.
Should not have
• Cluttered Layout: Overcrowding pages with too much information, images, or other elements can make your website look messy and confusing, hindering usability. Irrelevant Content: Your website should focus on information that is relevant to your target audience and industry. Avoid including content that does not provide value or enhance understanding of your products or services. Complex Navigation: A website should not have a confusing navigation system. Users should be able to find what they're looking for quickly and easily. Inconsistent Design: Inconsistencies in fonts, colors, or overall design can make your website look unprofessional. The design should be consistent throughout all pages. Slow Loading Times: Large images, animations, or other elements that significantly slow down page loading times should be avoided. Slow websites can lead to a poor user experience and high bounce rates. Poor Mobile Experience: Given the prevalence of mobile browsing, a design that doesn't perform well on mobile devices is a definite no. Autoplay Media: Videos or audio clips that start playing automatically can be annoying to users and should generally be avoided. Inaccessible Content: Ensure that all content is accessible to users of all abilities. Avoid design elements that violate accessibility standards. Hidden Contact Information: Contact information should be easy to find. Do not hide it in obscure parts of the website. Pop-ups: While sometimes necessary for marketing strategies, excessive use of pop-ups can annoy users and distract from the main content. Outdated Plugins: Avoid using outdated plugins or technology that some users may not be able to load or that could pose security risks. Lack of Privacy Policy: A website must have a clear and accessible privacy policy. Not having one can damage trust and may also violate laws or regulations.

```html
<!DOCTYPE html>
<html lang="en">
<head>
<meta charset="utf-8">
<title>Stridewell Equine Insurance</title>
<link rel="stylesheet" href="https://fonts.googleapis.com/css2?family=Oswald:wght@400;500;600&family=Poppins:wght@400;500;600;700&display=swap">
<style>
:root{
  --ink:#231f20;
  --text:#444;
  --muted:#777;
  --field:#efefef;
  --line:#cfcfcf;
  --white:#fff;
  --star:#f0a12b;
  --footer:#221e1f;
  --banner:#7a7a7a;
}
*{box-sizing:border-box;margin:0;padding:0}
html,body{width:1200px;height:4736px;overflow:hidden}
body{position:relative;background:var(--white);font-family:"Poppins",sans-serif;color:var(--text)}
.abs{position:absolute}
.heading{font-family:"Oswald",sans-serif;font-weight:500;color:var(--ink);text-transform:uppercase;letter-spacing:.3px}
.btn-outline{display:flex;align-items:center;justify-content:center;border:2px solid var(--ink);background:var(--white);font-weight:700;font-size:11.5px;color:var(--ink);text-transform:uppercase;letter-spacing:.2px}
.rule{display:block;width:40px;height:2px;background:#ddd;margin:10px auto 0}

/* header */
.site-header{left:0;top:0;width:1200px;height:110px;z-index:5}
.brand{left:88px;top:28px;display:flex;align-items:center;gap:10px}
.brand-dot{width:40px;height:40px;border-radius:50%;border:2px solid var(--ink)}
.brand-name{font-family:"Oswald",sans-serif;font-weight:500;font-size:34px;letter-spacing:3px;color:var(--ink);line-height:1}
.main-nav{left:408px;top:44px;display:flex;gap:24px;align-items:center;font-family:"Oswald",sans-serif;font-size:12.5px;line-height:1;color:var(--ink);text-transform:uppercase;font-weight:400;white-space:nowrap}
.login-btn{left:960px;top:33px;width:150px;height:39px;border:2px solid var(--ink);font-size:11.5px;font-weight:700;color:var(--ink);display:flex;align-items:center;justify-content:center;gap:8px;text-transform:uppercase;background:var(--white)}

/* hero */
.hero-photo{left:0;top:0;width:1200px;height:873px;clip-path:polygon(0 0,100% 0,100% 660px,0 873px);
  background:
   radial-gradient(ellipse 300px 260px at 870px 340px,#5a3a28 0%,rgba(90,58,40,.6) 45%,rgba(90,58,40,0) 75%),
   radial-gradient(ellipse 200px 200px at 650px 320px,#e9e4dc 0%,rgba(233,228,220,0) 70%),
   linear-gradient(180deg,#cfd3d4 0%,#b9bdb9 30%,#8a8a70 55%,#b69b63 75%,#9a7d48 100%)}
.hero-title{left:86px;top:222px;font-family:"Oswald",sans-serif;font-weight:500;font-size:88px;line-height:84px;color:var(--white);text-transform:uppercase;letter-spacing:1px}
.hero-sub{left:88px;top:498px;font-family:"Oswald",sans-serif;font-size:21px;color:var(--white);text-transform:uppercase;letter-spacing:.3px}
.hero-btn{left:88px;top:546px;width:140px;height:38px}

/* about */
.about-art{left:200px;top:880px;width:430px;height:430px;border-radius:50%;background:radial-gradient(circle at 50% 40%,#f1e6d6 0%,#d8b58c 40%,#9a4a26 70%,#6f4a2c 100%)}
.about-title{left:684px;top:912px;font-size:42px}
.about-text{left:684px;top:982px;width:392px;font-size:13.4px;line-height:20.2px}
.about-btn{left:684px;top:1230px;width:114px;height:38px}

/* services */
.section-title{left:0;width:1200px;text-align:center;font-size:42px}
.services-lede{left:300px;top:1498px;width:600px;text-align:center;font-size:13.4px;line-height:20px}
.cards{left:88px;top:1570px;width:1112px;height:460px;overflow:hidden}
.card-row{display:flex;gap:13px}
.service-card{flex:0 0 333px;background:var(--white);box-shadow:0 10px 30px rgba(0,0,0,.1);height:415px}
.service-photo{height:253px}
.service-body{padding:22px 24px}
.service-body h3{font-family:"Oswald",sans-serif;font-weight:500;font-size:17px;color:var(--ink);text-transform:uppercase;margin-bottom:12px}
.service-body p{font-size:13px;line-height:19.6px}
.purchase-btn{left:524px;top:2040px;width:152px;height:37px}

/* quote */
.quote-photo{left:0;top:2114px;width:1200px;height:901px;clip-path:polygon(0 0,100% 0,100% 626px,0 901px);
  background:
   radial-gradient(ellipse 260px 420px at 870px 400px,#6b3a1e 0%,rgba(107,58,30,.8) 45%,rgba(107,58,30,0) 80%),
   linear-gradient(180deg,#ffffff 0%,#e9ecee 12%,#c9d0d4 35%,#6f8a4c 60%,#5c7d33 80%,#84a24e 100%)}
.quote-card{left:86px;top:2178px;width:500px;height:588px;background:var(--white);box-shadow:0 10px 40px rgba(0,0,0,.12);padding:38px 44px}
.quote-card h2{text-align:center;font-size:42px;margin-bottom:26px}
.form-grid{display:grid;grid-template-columns:1fr 1fr;gap:20px 2px}
.field label{display:block;font-size:10.5px;font-weight:700;color:var(--ink);text-transform:uppercase;margin-bottom:6px}
.field .input{height:40px;background:var(--field);font-size:12px;color:#999;padding:0 18px;display:flex;align-items:center;justify-content:space-between}
.field.wide{grid-column:1/3}
.field .area{height:110px;align-items:flex-start;padding-top:14px}
.submit{margin-top:28px;height:44px;background:var(--ink);color:var(--white);font-size:12.5px;font-weight:700;display:flex;align-items:center;justify-content:center;position:relative;text-transform:uppercase}
.submit svg{position:absolute;right:16px;top:13px}

/* blog */
.blog-card{top:3073px;width:296px;height:401px;background:var(--white);box-shadow:0 10px 30px rgba(0,0,0,.1)}
.blog-photo{height:235px}
.blog-body{padding:26px 30px}
.blog-date{font-size:10.5px;color:var(--muted);margin-bottom:10px}
.blog-body h3{font-family:"Oswald",sans-serif;font-weight:500;font-size:15.5px;color:var(--ink);text-transform:uppercase;margin-bottom:8px}
.blog-body p{font-size:12.6px;line-height:19px}

/* reviews */
.quote-mark{font-family:"Oswald",sans-serif;font-size:260px;line-height:1;color:#eeeeee}
.review{width:414px}
.review p{font-size:13.4px;line-height:23px}
.review-name{font-size:11.5px;font-weight:700;color:var(--ink);text-transform:uppercase;margin-top:18px}
.stars{color:var(--star);font-size:19px;letter-spacing:1px;line-height:1.2}
.pager{left:1148px;top:3740px;display:flex;flex-direction:column;gap:11px}
.pager span{width:10px;height:10px;border-radius:50%;background:#ddd}
.pager span:first-child{background:var(--ink)}

/* claim banner */
.claim-banner{left:167px;top:4038px;width:864px;height:204px;background:var(--banner)}
.claim-horse{left:754px;top:3897px;width:240px;height:348px;border-radius:50% 40% 10% 10%;background:radial-gradient(ellipse at 55% 45%,#c0642a 0%,#8a3f18 45%,rgba(40,25,20,.85) 75%,rgba(40,25,20,0) 100%)}
.claim-title{left:255px;top:4060px;font-family:"Oswald",sans-serif;font-weight:500;font-size:64px;color:var(--white);line-height:1;text-transform:uppercase}
.claim-sub{left:255px;top:4136px;font-family:"Oswald",sans-serif;font-size:20px;color:var(--white);text-transform:uppercase}
.claim-btn{left:255px;top:4172px;width:177px;height:34px;background:var(--white);font-size:11.5px;font-weight:700;color:var(--ink);display:flex;align-items:center;justify-content:center;text-transform:uppercase}

/* footer */
.site-footer{left:0;top:4300px;width:1200px;height:436px;background:var(--footer);clip-path:polygon(0 0,100% 30px,100% 100%,0 100%);color:#cfcfcf}
.footer-brand{left:86px;top:126px;display:flex;align-items:center;gap:12px}
.footer-brand .brand-dot{border-color:var(--white);width:46px;height:46px}
.footer-brand .brand-name{color:var(--white);font-size:40px;letter-spacing:3px}
.socials{left:142px;top:228px;display:flex;gap:14px}
.socials span{width:32px;height:32px;border-radius:50%;border:1.5px solid #bdbdbd}
.footer-col h4{font-family:"Oswald",sans-serif;font-weight:500;font-size:18px;color:var(--white);text-transform:uppercase;margin-bottom:20px}
.footer-col li{list-style:none;font-size:12.5px;line-height:27px}
.contact-item{display:flex;gap:12px;font-size:12.5px;line-height:18px;margin-bottom:18px}
.contact-item svg{flex:0 0 12px;margin-top:3px}
.news-text{font-size:12.5px;line-height:18px;width:260px}
.news-input{margin-top:22px;width:246px;height:48px;background:#3a3637;display:flex;align-items:center;justify-content:space-between;padding:0 18px;font-size:12px;color:#ddd}
.copyright{left:0;top:402px;width:1200px;text-align:center;font-size:11.5px;font-weight:600;color:var(--white)}
.chat-btn{left:1123px;top:4635px;width:62px;height:62px;border-radius:50%;background:#bdbdbd;display:flex;align-items:center;justify-content:center;z-index:6}
</style>
</head>
<body>

<header class="abs site-header">
  <div class="abs brand"><span class="brand-dot"></span><span class="brand-name">STRIDEWELL</span></div>
  <nav class="abs main-nav">
    <svg width="14" height="13" viewBox="0 0 14 13"><path d="M7 0L0 6h2v7h4V9h2v4h4V6h2z" fill="#231f20"/></svg>
    <span>About Us</span><span>Services/Products</span><span>Get a Quote</span><span>File a Claim</span><span>Blog</span><span>Contact Us</span>
  </nav>
  <div class="abs login-btn"><svg width="11" height="12" viewBox="0 0 11 12"><circle cx="5.5" cy="3" r="3" fill="#231f20"/><path d="M0 12c0-4 2.5-5 5.5-5S11 8 11 12z" fill="#231f20"/></svg>Login Account</div>
</header>

<section class="hero">
  <div class="abs hero-photo" role="img" aria-label="Two horses, one pinto and one bay, galloping through tall golden grass below misty hills"></div>
  <h1 class="abs hero-title">Stridewell<br>Equine<br>Insurance</h1>
  <p class="abs hero-sub">Our next-generation equine insurance business</p>
  <a class="abs btn-outline hero-btn">Get a Quote</a>
</section>

<section class="about">
  <div class="abs about-art" role="img" aria-label="Chestnut horse galloping across an open field at sunset, framed in a circle"></div>
  <h2 class="abs heading about-title">About Us</h2>
  <p class="abs about-text">Lorem Ipsum is simply dummy text of the printing and typesetting industry. Lorem Ipsum has been the industry's standard dummy text ever since the 1500s, when an unknown printer took a galley of type and scrambled it to make a type specimen book. It has survived not only five centuries, but also the leap into electronic typesetting, remaining essentially unchanged. It was popularised in the 1960s with the release of Letraset sheets containing Lorem Ipsum passages, and more recently with desktop publishing software like Aldus PageMaker including versions of Lorem Ipsum.</p>
  <a class="abs btn-outline about-btn">Read More</a>
</section>

<section class="services">
  <h2 class="abs heading section-title" style="top:1424px">Services Stridewell</h2>
  <p class="abs services-lede">We offer customized equine insurance policies to protect your horses and your financial interests. Trust us for comprehensive coverage tailored to your needs.</p>
  <div class="abs cards">
    <div class="card-row">
      <article class="service-card">
        <div class="service-photo" role="img" aria-label="A bay horse and a grey horse grazing in a green paddock" style="background:linear-gradient(180deg,#7f9a5a,#5a4030 55%,#6f8c45)"></div>
        <div class="service-body"><h3>Mortality Insurance</h3><p>Protect your horses from unexpected loss or death with our comprehensive coverage for accidents, illnesses, and natural causes.</p></div>
      </article>
      <article class="service-card">
        <div class="service-photo" role="img" aria-label="A veterinarian examining a chestnut horse while its owner looks on" style="background:linear-gradient(180deg,#9bb27a,#a5602e 45%,#2f5fb0 75%,#7b8f55)"></div>
        <div class="service-body"><h3>Medical Coverage</h3><p>Ensure your horses receive the best veterinary care with our insurance plans covering diagnostics, treatments, surgeries, medications, and rehabilitation.</p></div>
      </article>
      <article class="service-card">
        <div class="service-photo" role="img" aria-label="A rider in a black helmet standing beside a dark horse in an indoor arena" style="background:linear-gradient(180deg,#d4c6b2,#3a2a22 50%,#b8a48a)"></div>
        <div class="service-body"><h3>Liability Coverage</h3><p>Safeguard yourself against property damage or bodily injury claims caused by your horses with our liability insurance.</p></div>
      </article>
      <article class="service-card">
        <div class="service-photo" role="img" aria-label="A horse owner standing with a horse outdoors" style="background:linear-gradient(180deg,#a8b98a,#4a5a6a 55%,#7a8c5a)"></div>
        <div class="service-body"><h3>Custom Plans</h3><p>Get personalised policies tailored to your needs, providing flexible cover for your horse.</p></div>
      </article>
    </div>
  </div>
  <a class="abs btn-outline purchase-btn">Online Purchase</a>
</section>

<section class="quote">
  <div class="abs quote-photo" role="img" aria-label="A bay horse with a flowing mane standing in a green meadow"></div>
  <form class="abs quote-card">
    <h2 class="heading">Get a Quote</h2>
    <div class="form-grid">
      <div class="field"><label>Name</label><div class="input">Enter name</div></div>
      <div class="field"><label>Email</label><div class="input">Enter email</div></div>
      <div class="field"><label>Phone</label><div class="input">Enter phone</div></div>
      <div class="field"><label>Address</label><div class="input">Enter address</div></div>
      <div class="field"><label>Postcode</label><div class="input">Post code - Suburb</div></div>
      <div class="field"><label>Country</label><div class="input">Select country<svg width="9" height="6" viewBox="0 0 9 6"><path d="M1 1l3.5 3.5L8 1" stroke="#444" stroke-width="1.5" fill="none"/></svg></div></div>
      <div class="field wide"><label>Message</label><div class="input area">Type your text...</div></div>
    </div>
    <div class="submit">Submit Now<svg width="16" height="16" viewBox="0 0 16 16"><path d="M15 1L1 7l5 2 2 6z M6 9l9-8" stroke="#fff" stroke-width="1.5" fill="none" stroke-linejoin="round"/></svg></div>
  </form>
</section>

<section class="blog">
  <h2 class="abs heading section-title" style="top:2986px">Latest Blog Post<span class="rule"></span></h2>
  <article class="abs blog-card" style="left:138px">
    <div class="blog-photo" role="img" aria-label="A rider adjusting the bridle of a dark horse" style="background:linear-gradient(120deg,#3a2a22,#6a4a36 50%,#e8e2da)"></div>
    <div class="blog-body"><div class="blog-date">25-05-2022</div><h3>Some Heading Goes Here</h3><p>Lorem Ipsum is simply dummy text of the printing and Ipsum has been the industry's standard...</p></div>
  </article>
  <article class="abs blog-card" style="left:452px">
    <div class="blog-photo" role="img" aria-label="Two people checking a horse's hoof outside a stable" style="background:linear-gradient(180deg,#c9c2b4,#6a7a8a 55%,#8a6a4a)"></div>
    <div class="blog-body"><div class="blog-date">25-05-2022</div><h3>Some Heading Goes Here</h3><p>Lorem Ipsum is simply dummy text of the printing and Ipsum has been the industry's standard...</p></div>
  </article>
  <article class="abs blog-card" style="left:766px">
    <div class="blog-photo" role="img" aria-label="A man in a suit standing with a chestnut horse in a green field" style="background:linear-gradient(180deg,#b6cbd8,#a0582a 45%,#2a2f45 65%,#6f9a45)"></div>
    <div class="blog-body"><div class="blog-date">25-05-2022</div><h3>Some Heading Goes Here</h3><p>Lorem Ipsum is simply dummy text of the printing and Ipsum has been the industry's standard...</p></div>
  </article>
</section>

<section class="reviews">
  <h2 class="abs heading section-title" style="top:3548px">Customer Review<span class="rule"></span></h2>
  <div class="abs quote-mark" style="left:258px;top:3600px">&ldquo;</div>
  <div class="abs quote-mark" style="left:756px;top:3600px">&ldquo;</div>
  <div class="abs review" style="left:145px;top:3722px">
    <p>Aenean sollicitudin, lorem quis bibendum auctor, nisi elit consequat ipsum, nec sagittis sem nibh id elit. Duis sed odio sit amet nibh vulputate cursus a sit amet mauris. Morbi accumsan ipsum velit. Nam nec tellus a auctor a ornare odio. Sed non mauris vitae erat consequat auctor eu in elit. Class aptent taciti sociosqu...</p>
    <div class="review-name">Daniel Hartley</div><div class="stars">★★★★★</div>
  </div>
  <div class="abs review" style="left:643px;top:3722px">
    <p>Aenean sollicitudin, lorem quis bibendum auctor, nisi elit consequat ipsum, nec sagittis sem nibh id elit. Duis sed odio sit amet nibh vulputate cursus a sit amet mauris. Morbi accumsan ipsum velit. Nam nec tellus a auctor a ornare odio. Sed non mauris vitae erat consequat auctor eu in elit. Class aptent taciti sociosqu...</p>
    <div class="review-name">Liam Prescott</div><div class="stars">★★★★★</div>
  </div>
  <div class="abs pager"><span></span><span></span><span></span></div>
</section>

<section class="claim">
  <div class="abs claim-banner"></div>
  <div class="abs claim-horse" role="img" aria-label="A chestnut horse with a windswept black mane rearing up"></div>
  <h2 class="abs claim-title">Stridewell</h2>
  <p class="abs claim-sub">What type of claim are you reporting?</p>
  <a class="abs claim-btn">Insurance Claim</a>
</section>

<footer class="abs site-footer">
  <div class="abs footer-brand"><span class="brand-dot"></span><span class="brand-name">STRIDEWELL</span></div>
  <div class="abs socials"><span></span><span></span><span></span><span></span></div>
  <div class="abs footer-col" style="left:428px;top:86px">
    <h4>Quick Links</h4>
    <ul><li>Home</li><li>About Us</li><li>Our Services</li><li>Get a Quote</li><li>File a Claim</li><li>Blog</li></ul>
  </div>
  <div class="abs footer-col" style="left:616px;top:86px">
    <h4>Contact Info</h4>
    <div class="contact-item"><svg width="12" height="10" viewBox="0 0 12 10"><rect x=".5" y=".5" width="11" height="9" fill="none" stroke="#ccc"/><path d="M.5 .5L6 5l5.5-4.5" stroke="#ccc" fill="none"/></svg><div>Email:<br>info@examplecom</div></div>
    <div class="contact-item"><svg width="12" height="12" viewBox="0 0 12 12"><path d="M2 0l3 3-1.5 1.5a7 7 0 004 4L9 7l3 3-2 2C5 12 0 7 0 2z" fill="#ccc"/></svg><div>Phone:<br>+08 123-456-789</div></div>
    <div class="contact-item"><svg width="12" height="14" viewBox="0 0 12 14"><path d="M6 14S0 8 0 5a6 6 0 0112 0c0 3-6 9-6 9z" fill="#ccc"/><circle cx="6" cy="5" r="2" fill="#221e1f"/></svg><div>Location:<br>Some address line goes<br>United Kingdom</div></div>
  </div>
  <div class="abs footer-col" style="left:862px;top:86px">
    <h4>Newsletter</h4>
    <p class="news-text">Join our mailing list to learn about our latest projects and product offerings</p>
    <div class="news-input"><span>✉&nbsp; Enter your email...</span><svg width="14" height="14" viewBox="0 0 16 16"><path d="M15 1L1 7l5 2 2 6z" fill="#fff"/></svg></div>
  </div>
  <p class="abs copyright">© 2023 &nbsp;All Rights Reserved</p>
</footer>

<div class="abs chat-btn" aria-label="Chat support"><svg width="30" height="26" viewBox="0 0 30 26"><path d="M3 2h24v16H12l-6 6v-6H3z" fill="#fff"/><circle cx="10" cy="10" r="1.8" fill="#999"/><circle cx="15" cy="10" r="1.8" fill="#999"/><circle cx="20" cy="10" r="1.8" fill="#999"/></svg></div>

</body>
</html>
```